Disposable food packaging business needs a product box design

We are looking for the design layout for our coffee cup cartons. They will be printed on white boxes and we would like them to be recognizable from a distance. These will not be seen by the customers buying coffee and the design is primarily for the Warehouse staff.
see attached a basic mockup and the type of cups that will be inside the cartons, creative freedom is still welcome, we are trying to achieve a more professional look.
Box size will be approximately 46cm wide, 50cm high and 38cm depth.
Things we would like.
- We would like our brand name 'KWT' to be one of the first things you notice. looking for a design for the brand/ logo.
-Each cup comes in multiple colours (black, white, rainbow, kraft (brown), we would like each box to have the colour of the cup incorporated into the design as well as the colour in writing. So that the colour of the cups is obvious.
-Each cup comes in multiple sizes (4oz, 6oz, 8oz, 8oz squat, 12oz and 16oz) that will need to be easily seen.
-A re-order code (example; RQB473).
-Carton quantity 1000 and inner sleeve qty 50.
-A barcode.
-Include attached symbols (eco friendly symbol to be black to match the rest).
So eventually there will be a total of 24 different coffee cup boxes- each with the same basic info.
-KWT brand
-Cup Colour (White, black, kraft and rainbow)
-Cup size (4, 6, 8, 8 squat, 12 and 16)
-Cup code (RQBxxx- xxx will be different for each cup/size)
-Carton qty 1000 sleeve qty 50 (same for every size and colour.
-Barcode (supplied later)
Initially just provide the generic design/ layout of one box- the successful designer will need to produce the design for all combinations.
NOTE - we are looking for the design of the outer carton for coffee cups. These cartons are for delivery of cups to cafes etc. They are not seen by the customer who purchases a coffee. The main requirement is for the warehouse staff to be able to easily identify and select the correct style and colour of cups.
Each carton contains 1000 cups.
Allow time for more entries.

```html
<!DOCTYPE html>
<html lang="en">
<head>
<meta charset="utf-8">
<title>KWT Coffee Cups – Carton Layout</title>
<link rel="stylesheet" href="https://fonts.googleapis.com/css2?family=Arimo:wght@400;700&display=swap">
<style>
  :root {
    --ink: #2b2523;
    --rule: #6b6b6b;
    --paper: #ffffff;
    --cup-area: #eeeceb;
  }
  html, body {
    margin: 0;
    padding: 0;
    width: 1200px;
    height: 571px;
    overflow: hidden;
    background: var(--paper);
  }
  .carton-layout {
    display: block;
    width: 1200px;
    height: 571px;
    font-family: "Arimo", Arial, sans-serif;
  }
  .dieline line, .dieline polyline { stroke: var(--rule); stroke-width: 0.6; fill: none; }
  .dimension line { stroke: var(--rule); stroke-width: 0.5; }
  .dimension-label { font-size: 15px; fill: #333; text-anchor: middle; }
  .dimension-gap { fill: var(--paper); }
  .brand { font-weight: 700; fill: var(--ink); }
  .headline { font-weight: 700; fill: var(--ink); }
  .spec-frame { fill: none; stroke: var(--ink); stroke-width: 1.5; }
  .spec-title { font-size: 14px; fill: var(--ink); }
  .spec-option { font-size: 11px; fill: var(--ink); }
  .tickbox { fill: none; stroke: var(--ink); stroke-width: 1; }
  .tick { fill: none; stroke: var(--ink); stroke-width: 1.6; stroke-linecap: round; stroke-linejoin: round; }
  .symbol-label { font-weight: 700; fill: var(--ink); }
  .symbol-fill { fill: var(--ink); }
  .eco-badge { fill: none; stroke: var(--ink); stroke-width: 1.4; }
  .cup-placeholder { fill: var(--cup-area); }
  .cup-size { font-weight: 700; fill: var(--ink); }
</style>
</head>
<body>
<svg class="carton-layout" viewBox="0 0 1200 571" xmlns="http://www.w3.org/2000/svg" role="img" aria-label="KWT coffee cup carton layout, 12oz white">
  <defs>
    <g id="side-panel">
      <text class="brand" x="74" y="239" font-size="49" textLength="95" lengthAdjust="spacingAndGlyphs">KWT</text>
      <text class="headline" x="172" y="239" font-size="19" textLength="123" lengthAdjust="spacingAndGlyphs">COFFEE CUPS</text>

      <rect class="spec-frame" x="75.5" y="248.5" width="219" height="120.5"/>
      <line class="spec-frame" x1="75.5" y1="288.5" x2="294.5" y2="288.5"/>
      <line class="spec-frame" x1="75.5" y1="347.5" x2="294.5" y2="347.5"/>

      <text class="spec-title" x="82.5" y="266">Cup Colour</text>
      <rect class="tickbox" x="84" y="273" width="10" height="10" rx="1"/>
      <polyline class="tick" points="85.5,277.5 88.5,281.5 95,270"/>
      <text class="spec-option" x="97.5" y="283">White</text>
      <rect class="tickbox" x="139" y="273" width="10" height="10" rx="1"/>
      <text class="spec-option" x="152" y="283">black</text>
      <rect class="tickbox" x="189.5" y="273" width="10" height="10" rx="1"/>
      <text class="spec-option" x="203" y="283">kraft</text>
      <rect class="tickbox" x="238.5" y="273" width="10" height="10" rx="1"/>
      <text class="spec-option" x="251.5" y="283">rainbow</text>

      <text class="spec-title" x="84" y="306">Cup size</text>
      <rect class="tickbox" x="85" y="314" width="10" height="10" rx="1"/>
      <text class="spec-option" x="98.5" y="324">4oz</text>
      <rect class="tickbox" x="171" y="314" width="10" height="10" rx="1"/>
      <text class="spec-option" x="184.5" y="324">6oz</text>
      <rect class="tickbox" x="251" y="314" width="10" height="10" rx="1"/>
      <text class="spec-option" x="264.5" y="324">8oz</text>
      <rect class="tickbox" x="85" y="330.5" width="10" height="10" rx="1"/>
      <text class="spec-option" x="98.5" y="340.5">8oz squat</text>
      <rect class="tickbox" x="171" y="330.5" width="10" height="10" rx="1"/>
      <polyline class="tick" points="172.5,335 175.5,339 182,327.5"/>
      <text class="spec-option" x="184.5" y="340.5">12oz</text>
      <rect class="tickbox" x="251" y="330.5" width="10" height="10" rx="1"/>
      <text class="spec-option" x="264.5" y="340.5">16oz</text>

      <text class="spec-title" x="84" y="364">Cup code RQBxxx- xxx</text>

      <text class="spec-option" x="79" y="394">Barcode</text>

      <path class="symbol-fill" d="M144.5,385.5 C146,389 149,392 149,395.5 A4.5,4.5 0 0 1 140,395.5 C140,392 143,389 144.5,385.5 Z"/>
      <text class="symbol-label" x="151.5" y="399" font-size="5.2" textLength="22" lengthAdjust="spacingAndGlyphs">Aqueous</text>
      <rect class="symbol-fill" x="180" y="386" width="10" height="14" rx="2"/>
      <text class="symbol-label" x="195" y="399" font-size="5.2" textLength="48" lengthAdjust="spacingAndGlyphs">Home compostable</text>
      <circle class="eco-badge" cx="256.5" cy="393.5" r="6.5"/>
      <text class="symbol-label" x="265" y="399" font-size="5.2" textLength="30" lengthAdjust="spacingAndGlyphs">Eco friendly</text>
    </g>

    <g id="front-panel">
      <text class="brand" x="328" y="262" font-size="78" textLength="156" lengthAdjust="spacingAndGlyphs">KWT</text>
      <text class="headline" x="329" y="289" font-size="25" textLength="154" lengthAdjust="spacingAndGlyphs">COFFEE CUPS</text>
      <text class="headline" x="329" y="317" font-size="19" textLength="61" lengthAdjust="spacingAndGlyphs">RQB473</text>
      <text class="headline" x="329" y="346" font-size="18" textLength="154" lengthAdjust="spacingAndGlyphs">QUANTITY 1000 cups</text>
      <text class="headline" x="329" y="363" font-size="18" textLength="110" lengthAdjust="spacingAndGlyphs">( 50 X 20 cups )</text>

      <g class="cup-mark">
        <rect class="cup-placeholder" x="492" y="205" width="104" height="164" rx="4" role="img" aria-label="Illustration of a paper coffee cup"/>
        <text class="cup-size" transform="translate(537,298) rotate(90)" x="-57" y="0" font-size="46" textLength="114" lengthAdjust="spacingAndGlyphs">12 OZ</text>
        <text class="cup-size" transform="translate(518,298) rotate(90)" x="-57" y="0" font-size="23" textLength="114" lengthAdjust="spacingAndGlyphs">WHITE S/W</text>
      </g>

      <path class="symbol-fill" d="M337.5,375 C340,381 345,386 345,393 A7.5,7.5 0 0 1 330,393 C330,386 335,381 337.5,375 Z"/>
      <text class="symbol-label" x="349" y="398" font-size="9.5" textLength="37" lengthAdjust="spacingAndGlyphs">Aqueous</text>
      <rect class="symbol-fill" x="396" y="375" width="19" height="26" rx="3"/>
      <text class="symbol-label" x="421" y="398" font-size="9.5" textLength="79" lengthAdjust="spacingAndGlyphs">Home compostable</text>
      <circle class="eco-badge" cx="520" cy="390" r="12.5"/>
      <text class="symbol-label" x="538" y="398" font-size="9.5" textLength="48" lengthAdjust="spacingAndGlyphs">Eco friendly</text>
    </g>
  </defs>

  <g class="dimension">
    <line x1="53" y1="32" x2="1157" y2="32"/>
    <line x1="53" y1="22" x2="53" y2="41"/>
    <line x1="317" y1="22" x2="317" y2="41"/>
    <line x1="605" y1="22" x2="605" y2="41"/>
    <line x1="870" y1="22" x2="870" y2="41"/>
    <line x1="1157" y1="22" x2="1157" y2="41"/>
    <rect class="dimension-gap" x="160" y="22" width="50" height="20"/>
    <rect class="dimension-gap" x="427" y="22" width="68" height="20"/>
    <rect class="dimension-gap" x="712" y="22" width="50" height="20"/>
    <rect class="dimension-gap" x="979" y="22" width="68" height="20"/>
    <text class="dimension-label" x="185" y="38">46cm</text>
    <text class="dimension-label" x="461" y="38">50cm</text>
    <text class="dimension-label" x="737" y="38">46cm</text>
    <text class="dimension-label" x="1013" y="38">50cm</text>

    <line x1="37" y1="47" x2="37" y2="553"/>
    <line x1="28" y1="47" x2="47" y2="47"/>
    <line x1="28" y1="191" x2="47" y2="191"/>
    <line x1="28" y1="409" x2="47" y2="409"/>
    <line x1="28" y1="553" x2="47" y2="553"/>
    <rect class="dimension-gap" x="27" y="90" width="20" height="60"/>
    <rect class="dimension-gap" x="27" y="270" width="20" height="60"/>
    <rect class="dimension-gap" x="27" y="452" width="20" height="60"/>
    <text class="dimension-label" transform="translate(43,119) rotate(-90)">25cm</text>
    <text class="dimension-label" transform="translate(43,300) rotate(-90)">38cm</text>
    <text class="dimension-label" transform="translate(43,481) rotate(-90)">25cm</text>
  </g>

  <g class="dieline">
    <line x1="53" y1="47" x2="53" y2="553"/>
    <line x1="317" y1="47" x2="317" y2="553"/>
    <line x1="605" y1="47" x2="605" y2="553"/>
    <line x1="870" y1="47" x2="870" y2="553"/>
    <line x1="1157" y1="47" x2="1157" y2="553"/>
    <line x1="53" y1="47" x2="1157" y2="47"/>
    <line x1="53" y1="191" x2="1157" y2="191"/>
    <line x1="53" y1="409" x2="1157" y2="409"/>
    <line x1="53" y1="553" x2="1157" y2="553"/>
    <polyline points="1157,191 1180,191 1180,409 1157,409"/>
  </g>

  <use href="#side-panel"/>
  <use href="#front-panel"/>
  <use href="#side-panel" transform="translate(552,0)"/>
  <use href="#front-panel" transform="translate(552,0)"/>
</svg>
</body>
</html>
```